Product labels for new supplements business targeting high performing creative people

I need a label design for different supplements like Whey, BCAA, Melatonin etc. that I could customize for each use case separately.

The brand is called lanternfolk.life, and it would be the first design of the labels. We haven't sold any products yet, but the target audience is people with growth mindset, people who want to be as efficient as possible and are constantly looking to improve their lifestyle. As part of that, they are also working out, but don't know much about supplements yet. Mostly people between 20-34.

I don't have a too specific idea of the expected design, though it should be light, warm, smart and minimalist, maybe have some patterns. It should looks smart and clean (and expensive). Orange and golden might be the additional colors for white. I have attached the templates of some products that I plan to sell and also the logo of the brand.

Here's what I have used for inspiration:
Brands that I like and are somewhat similar in concept: https://www.vimqera.com/ (!!specially the way they
bring "how the product helps them" in focus, not "what the product is" & https://www.pobri.care/ &
https://www.selvoda.com/sport/ & https://en.kambelo.fr/ &
https://gridmarket.com/profiles/corawellhaldesign/designs/417586

Here's how different products look like: https://prodaxel.com/catalog

Target Market(s)

target audience is people with growth mindset, people who want to be as efficient as possible and are constantly looking to improve their lifestyle. As part of that, they are also working out, but don't know much about supplements yet. Mostly people between 20-34.

Industry/Entity Type

Supplements

Font styles to use
Sans Serif

Colors
FFC000
F8CF3A
FAE287
FDF2CF
FEFAEE
F0912C
F2A743
F7CA91
FBE8D2
FDF5EE
EE7325
F08F49
F5BC92
FAE3D3
FDF4ED

Requirements
Must have
• Clean, smart and minimalist design that can be applied for different products in different sizes, like Whey protein, BCAA, vitamins etc. available here: https://prodaxel.com/catalog
Nice to have
• Patterns, expensive look
Should not have
• Doodles, too many colors

```html
<!DOCTYPE html>
<html lang="en">
<head>
<meta charset="utf-8">
<title>lanternfolk.life — Maca Root Powder label</title>
<link rel="stylesheet" href="https://fonts.googleapis.com/css2?family=Montserrat:wght@200;300;400;600;700&family=Open+Sans:wght@400;600&family=Roboto+Condensed:wght@400&family=Arimo:wght@400;700&display=swap">
<style>
  :root {
    --label-orange: #f05c05;
    --ink: #1a1a1a;
    --paper: #ffffff;
    --canvas: #f6f6f6;
  }
  * { box-sizing: border-box; margin: 0; padding: 0; }
  html, body { width: 1200px; height: 1200px; overflow: hidden; background: var(--canvas); }
  .canvas { position: relative; width: 1200px; height: 1200px; }
  .label {
    position: absolute; left: 50%; top: 50%;
    width: 1274px; height: 517px;
    margin-left: -637px; margin-top: -258.5px;
    transform: scale(0.91);
    background: var(--label-orange);
    color: var(--ink);
    font-family: "Open Sans", sans-serif;
  }
  .label > * { position: absolute; }

  .brand-tab {
    left: 422px; top: 0; width: 193px; height: 47px;
    background: var(--paper);
    display: flex; align-items: center; justify-content: center; gap: 8px;
  }
  .brand-tab .brand-square { width: 16px; height: 16px; background: var(--label-orange); }
  .brand-tab .brand-name { font-family: "Montserrat", sans-serif; font-weight: 600; font-size: 19px; color: #333; }

  .section-tag {
    background: var(--paper); color: var(--label-orange);
    font-family: "Montserrat", sans-serif; font-weight: 300;
    font-size: 16px; letter-spacing: 1px; line-height: 23px;
    padding: 0 6px; border-radius: 2px;
  }
  .tag-use { left: 31px; top: 47px; }
  .tag-caution { left: 31px; top: 170px; }
  .copy { font-size: 15.2px; line-height: 19.6px; text-align: justify; }
  .copy-use { left: 53px; top: 75px; width: 307px; }
  .copy-caution { left: 31px; top: 197px; width: 352px; }
  .copy-warning {
    left: 31px; top: 302px; width: 352px;
    font-family: "Roboto Condensed", sans-serif; font-size: 15.4px; line-height: 19.6px;
  }
  .fda-note { left: 56px; top: 390px; width: 302px; font-size: 12.4px; line-height: 19.6px; text-align: justify; }

  .title-word {
    font-family: "Montserrat", sans-serif; font-weight: 400;
    color: var(--paper); font-size: 119px; line-height: 1; letter-spacing: 23px;
  }
  .title-maca { left: 416px; top: 125px; }
  .title-root { left: 424px; top: 224px; letter-spacing: 21px; }
  .title-powder {
    left: 514px; top: 287px;
    font-family: "Montserrat", sans-serif; font-weight: 200;
    font-size: 50px; letter-spacing: 3px; color: var(--ink); line-height: 1;
  }
  .claims {
    left: 415px; top: 410px;
    font-family: "Montserrat", sans-serif; font-weight: 300;
    color: var(--paper); font-size: 16px; letter-spacing: 1.3px; line-height: 20px;
  }
  .product-type {
    left: 415px; top: 463px;
    font-family: "Montserrat", sans-serif; font-weight: 700;
    color: var(--paper); font-size: 16px; letter-spacing: 1.6px;
  }
  .net-weight {
    left: 792px; top: 469px;
    font-family: "Montserrat", sans-serif; font-weight: 700;
    color: var(--paper); font-size: 20px; letter-spacing: 1px;
  }

  .facts {
    left: 913px; top: 32px; width: 351px; height: 293px;
    border: 2px solid var(--ink);
    font-family: "Arimo", sans-serif; color: var(--ink);
    padding: 3px 6px 0 6px;
  }
  .facts h2 { font-weight: 700; font-size: 35px; line-height: 40px; letter-spacing: 0.3px; }
  .facts .serving { font-size: 15px; line-height: 17px; margin-top: 10px; }
  .facts .thick-rule { height: 5px; background: var(--ink); margin: 5px -4px 0; }
  .facts table { width: 100%; border-collapse: collapse; font-size: 15px; }
  .facts th { font-weight: 700; font-size: 14.5px; line-height: 13px; text-align: right; padding: 4px 0 3px; vertical-align: bottom; }
  .facts thead tr { border-bottom: 3px solid var(--ink); }
  .facts td { line-height: 18px; padding: 0; border-bottom: 1px solid var(--ink); }
  .facts td.amount { text-align: right; }
  .facts td.dv { text-align: right; width: 70px; font-size: 11px; vertical-align: top; }
  .facts tbody tr:last-child { border-bottom: 3px solid var(--ink); }
  .facts .notes { font-size: 14.5px; line-height: 13px; margin-top: 8px; }
  .facts .notes p + p { margin-top: 8px; }
  .other-ingredient { left: 921px; top: 332px; font-family: "Arimo", sans-serif; font-size: 15px; }
  .distributor {
    left: 895px; top: 467px; width: 360px; text-align: center;
    font-size: 12.4px; line-height: 17px;
  }
</style>
</head>
<body>
<main class="canvas">
  <section class="label" aria-label="Maca Root Powder product label">
    <div class="brand-tab"><span class="brand-square"></span><span class="brand-name">lanternfolk.life</span></div>

    <span class="section-tag tag-use">SUGGESTED USE:</span>
    <p class="copy copy-use">Eat up to 10g of maca powder a day. It can be added to cocktails and granola. Do not use this product as a substitute for a complete and balanced diet.</p>

    <span class="section-tag tag-caution">CAUTION:</span>
    <p class="copy copy-caution">Do not exceed recommended dose. Pregnant or nursing mothers, children under the age of 18, and individuals with a known medical condition should consult a physician before using this or any dietary supplement.</p>
    <p class="copy-warning">KEEP OUT OF REACH OF CHILDREN. DO NOT USE IF SAFETY SEAL IS DAMAGED OR MISSING. STORE IN A COOL, DRY PLACE.</p>
    <p class="fda-note">* These statements have not been evaluated by the Food and Drug Administration. This product is not intended to diagnose, treat, cure or prevent any disease.</p>

    <h1 class="title-word title-maca">MACA</h1>
    <span class="title-word title-root">ROOT</span>
    <span class="title-powder">POWDER</span>

    <p class="claims">Helps reduce stress*<br>Increases energy and stamina*</p>
    <p class="product-type">DIETARY SUPPLEMENT</p>
    <p class="net-weight">200g</p>

    <div class="facts">
      <h2>Supplement Facts</h2>
      <p class="serving">Serving Size: 10 g<br>Servings per container: 20</p>
      <div class="thick-rule"></div>
      <table>
        <thead>
          <tr><th></th><th>Amount per<br>Serving*</th><th>% Daily<br>Value</th></tr>
        </thead>
        <tbody>
          <tr><td>Calories</td><td class="amount">45 Kcal</td><td class="dv">**</td></tr>
          <tr><td>Carbohydrate</td><td class="amount">9 g</td><td class="dv">**</td></tr>
          <tr><td>Calcium</td><td class="amount">24 mg</td><td class="dv">**</td></tr>
          <tr><td>Iron</td><td class="amount">3 mg</td><td class="dv">**</td></tr>
          <tr><td>Potassium</td><td class="amount">210 mg</td><td class="dv">**</td></tr>
        </tbody>
      </table>
      <div class="notes">
        <p>*Best use scales to determine the exact weight per serving</p>
        <p>**Daily Value not established</p>
      </div>
    </div>
    <p class="other-ingredient">Other Ingredient: 100% Maca root</p>

    <p class="distributor">Manufactured for and distributed by: [your LLC name here]<br>Address: [your legal address and phone nr or email]</p>
  </section>
</main>
</body>
</html>
```